Zielgruppe
Wir sind eine Full-Service Ferienhaus-Agentur welches sich auf die Vermietung & Vermarktung von Ferienimmobilien an der Schlei und Ostsee spezialisiert hat.
Aufgabenstellung
Der Flyer soll in den Farben von www.feldmark-beratung.de gestaltet werden, ebenfalls mit den dort abgebildeten Texten (die 6 Felder). Das Firmenlogo und Kontaktdaten können von der Seite genommen werden.
Der Flyer soll an interessierte Immobilienbesitzer ausgegeben werden.
Folgender Textabschnitt soll noch mit aufgenommen werden:
Unsere Preise im Überblick:
Wir nehmen eine Provision von 20 % inkl. Mehrwertsteuer auf die vereinnahmte Miete.
Auf Nebenleistungen ist keine Provision fällig. So ist sichergestellt, dass wir ein maximales Interesse an einer hohen Auslastung Ihres Objektes haben, da wir nur Geld verdienen, wenn auch Sie Geld verdienen.
Für die besagten 20 % haben Sie nichts mehr mit den Themen Vermarktung, Anfragen, Geldeingang, Kundenfragen oder Endreinigung zu tun.

```html
<!DOCTYPE html>
<html lang="de">
<head>
<meta charset="utf-8">
<title>Feldmark Beratung – Flyer</title>
<link href="https://fonts.googleapis.com/css2?family=Barlow:ital,wght@0,400;0,600;0,700;1,500;1,600;1,700&display=swap" rel="stylesheet">
<style>
  :root {
    --page-bg: #e9e6e2;
    --paper: #ffffff;
    --band-blue: #4f84b8;
    --head-blue: #2b7cc4;
    --ink: #1f1f1f;
    --logo-ink: #1a1a1a;
    --white: #ffffff;
  }
  * { margin: 0; padding: 0; box-sizing: border-box; }
  html, body { width: 706px; height: 1200px; overflow: hidden; background: var(--page-bg); }
  body { position: relative; font-family: "Barlow", sans-serif; color: var(--ink); }

  .spread {
    position: absolute; left: 0; top: 247px;
    width: 1000px; height: 1000px;
    transform: scale(0.706); transform-origin: 0 0;
    display: flex;
  }
  .panel { position: relative; width: 500px; height: 1000px; overflow: hidden; background: var(--paper); }

  /* Front panel */
  .cover-photo {
    position: absolute; inset: 0;
    background: linear-gradient(180deg,
      #d9dcdf 0%, #cfd3d6 28%, #a7b3bb 34%, #8e9ea7 42%,
      #b3aea4 50%, #a58a66 62%, #9a7a55 78%, #8a6e4d 100%);
  }
  .wave { position: absolute; left: 0; top: 0; width: 500px; height: 1000px; }
  .wave path { fill: var(--band-blue); }

  .brand {
    position: absolute;
    font-family: "Barlow", sans-serif;
    font-weight: 600;
    color: var(--logo-ink);
    text-transform: uppercase;
    line-height: 1;
    display: flex; align-items: center; gap: 12px;
  }
  .brand-dot { width: 14px; height: 14px; border-radius: 50%; background: var(--logo-ink); flex: none; }
  .brand-name { display: block; letter-spacing: 1px; }
  .brand--cover { left: 120px; top: 120px; font-size: 46px; }
  .brand--back { left: 258px; top: 790px; font-size: 38px; }

  .tagline {
    position: absolute; left: 60px; top: 934px;
    font-weight: 700; font-style: italic; font-size: 18px;
    letter-spacing: 0.6px; color: var(--white); text-transform: uppercase;
  }

  /* Back panel */
  .columns { position: absolute; left: 48px; top: 50px; display: flex; gap: 22px; }
  .col { width: 190px; }
  .col + .col { width: 195px; }
  .block { margin-bottom: 18px; }
  .block h2 {
    font-weight: 500; font-style: italic; font-size: 15px; line-height: 18.5px;
    letter-spacing: 0.7px; text-transform: uppercase; color: var(--head-blue);
    margin-bottom: 5px;
  }
  .block p { font-size: 14.5px; line-height: 18.5px; letter-spacing: 0.2px; margin-bottom: 7px; }

  .service-line {
    position: absolute; left: 48px; top: 910px;
    font-weight: 600; font-style: italic; font-size: 12.5px; line-height: 16px;
    color: var(--white); text-transform: uppercase;
  }
  .contact {
    position: absolute; left: 260px; top: 883px;
    font-weight: 600; font-size: 13px; line-height: 20.5px; color: var(--white);
    font-style: normal;
  }
</style>
</head>
<body>
  <div class="spread">
    <section class="panel panel--front">
      <div class="cover-photo" role="img" aria-label="Foto: reetgedecktes Strandhaus in den Dünen mit trockenem Strandhafer, Buhnen und Ostsee im Hintergrund"></div>
      <div class="brand brand--cover"><span class="brand-dot"></span><span class="brand-name">Feldmark<br>Beratung</span></div>
      <svg class="wave" viewBox="0 0 500 1000" aria-hidden="true">
        <path d="M0 908 C150 900 330 840 500 722 L500 1000 L0 1000 Z"/>
      </svg>
      <p class="tagline">Geben Sie Ihr Domizil in gute Hände!</p>
    </section>

    <section class="panel panel--back">
      <svg class="wave" viewBox="0 0 500 1000" aria-hidden="true">
        <path d="M0 902 C180 895 380 830 500 730 L500 1000 L0 1000 Z"/>
      </svg>
      <div class="columns">
        <div class="col">
          <div class="block">
            <h2>›Wir übernehmen für Sie die komplette Abwicklung‹</h2>
            <p>Sei es Buchung, Zahlungs­empfang, Schlüsselüber­gabe, Endreinigung oder Kundenkommunikation. Der gesamte Kundenservice läuft über uns.</p>
          </div>
          <div class="block">
            <h2>›Sie sind jederzeit aktuell informiert‹</h2>
            <p>Über jede neue Buchung werden Sie automatisch per E-Mail informiert. Zudem können Sie den bequemen Ei­gentümerlogin jederzeit Ihre Buchungen &amp; bereits erhalte­nen Abrechnungen einsehen und auf Wunsch Zeiten für sich selbst reservieren.</p>
          </div>
          <div class="block">
            <h2>›Kundenservice 7 Tage die Woche‹</h2>
            <p>Wir sind vom guten Kunden­service überzeugt. Ob Ei­gentümer oder Gast, bei uns ist jeder in guten Händen. Sie erreichen uns 7 Tage die Woche. Per Telefon, E-Mail oder Messenger.</p>
          </div>
          <div class="block">
            <h2>›Maximale Präsenz für Ihre Objekte‹</h2>
            <p>Wir erreichen unsere Gäste über unser eigenes Portal www.foerde-urlaub.de und arbeiten darüber hinaus mit diversen großen Portalen wie Reisebucht.com, Ferienwelt-Wohnungen, Urlaub-mit-Tier oder meinUrlaubshaus.de zusammen.</p>
          </div>
        </div>
        <div class="col">
          <div class="block">
            <h2>›Wir sind offen für neue Trends‹</h2>
            <p>Denn wir nicht mit der Zeit geht, geht mit der Zeit. Wir beobachten die Marktent­wicklung und können flexibel drauf reagieren.</p>
          </div>
          <div class="block">
            <h2>›Bei uns sind Sie und Ihre Immobilie in den besten Händen‹</h2>
            <p>Und das Ganze mit einer leistungsbezogenen Abrech­nung. Mit unserem Provisi­onsmodell verdienen wir nur Geld, wenn wir Ihre Immobi­lie effektiv vermieten!</p>
          </div>
          <div class="block">
            <h2>Unsere Preise im Überblick</h2>
            <p>Wir nehmen eine Provision von 20 % inkl. Mehrwertsteuer auf die vereinnahmte Miete.</p>
            <p>Auf Nebenleistungen ist keine Provision fällig. So ist sichergestellt, dass wir ein maximales Interesse an ei­ner hohen Auslastung Ihres Objektes haben, da wir nur Geld verdienen, wenn auch Sie Geld verdienen.</p>
            <p>Für die besagten 20 % haben Sie nichts mehr mit den The­men Vermarktung, Anfragen, Geldeingang, Kundenfragen oder Endreinigung zu tun.</p>
          </div>
        </div>
      </div>
      <div class="brand brand--back"><span class="brand-name">Feldmark<br>Beratung</span></div>
      <p class="service-line">Vermietung &amp; Vermarktung<br>von Ferienimmobilien an der<br>Schlei und Ostsee</p>
      <address class="contact">
        Lindenweg 14, 24376 Wiesenau<br>
        T. 0151 2 34 56 789<br>
        info@feldmark-beratung.de<br>
        www.feldmark-beratung.de
      </address>
    </section>
  </div>
</body>
</html>
```